1 großer und 2 kleine Banner für Startseite von Schlaufenhof12
Zielgruppe
Großhandel für Klett- und Gurtband mit einer Auswahl von über 2.500 Artikel. Unsere Onlinekunden sind zu 80% weiblich und kommen aus dem kreativen Nähbereich. Aus den Materialien werden z.B. Hundeleinen, Pferdegeschirr und Taschen genäht. Zu unseren Kunden zählen aber auch große Gewerbekunden aus anderen Bereichen.
Aufgabenstellung
Wir benötigen einen Banner für die Startseite. Bei dem Banner geht es um den Frühling und die Frühlingsfarben unserer Bänder und Schnüre. Leider kann ich Ihnen hier nur die Produktbilder zur Verfügung stellen. Freigestellte Bilder habe ich nicht. Produkte aus folgenden Kategorien sollen beworben werden (Frühlingsfarben und auch das neue Petrol): https://www.schlaufenhof12.de/baender/gurtband/pp-gurtband-1-4mm-stark/25mm-breit/10m-rollen/ und Schnüre: https://www.schlaufenhof12.de/schnur-kordeln/pp-schnur/5mm-pp-schnur/50m/?p=1
Der Banner hat folgende Maße: 870x580
Weiterhin benötigen wir 2 kleinere Banner 580 x 180:
Banner 1 soll für „Restposten“ werben und Banner 2 für „Sonderposten“. Es sollte im Design unserer Seite sein und muss nicht unbedingt Artikel zeigen.

```html
<!DOCTYPE html>
<html lang="de">
<head>
<meta charset="utf-8">
<title>Restposten – Schlaufenhof12</title>
<link rel="stylesheet" href="https://fonts.googleapis.com/css2?family=Open+Sans:wght@600;700&display=swap">
<style>
  :root {
    --photo-dark: #2a2a2e;
    --band-teal: #2fb39a;
    --band-grey: #6c6f73;
    --band-navy: #1f2d52;
    --band-red: #b8232b;
    --band-olive: #6b6a3a;
    --band-cream: #e8e1cf;
    --accent: #c8711c;
    --accent-dark: #a95a12;
    --white: #ffffff;
  }
  html, body {
    margin: 0;
    padding: 0;
    overflow: hidden;
    background: var(--white);
  }
  .banner {
    position: relative;
    width: 1200px;
    height: 372px;
    overflow: hidden;
    font-family: "Open Sans", Arial, sans-serif;
  }
  .banner__photo {
    position: absolute;
    inset: 0;
    background:
      linear-gradient(90deg,
        rgba(0,0,0,0.25) 0%, rgba(0,0,0,0) 12%),
      linear-gradient(180deg,
        var(--band-teal) 0%, var(--band-teal) 18%,
        var(--band-grey) 18%, var(--band-grey) 38%,
        var(--band-navy) 38%, var(--band-navy) 58%,
        #5a3a2a 58%, #5a3a2a 78%,
        var(--band-red) 78%, var(--band-red) 100%);
  }
  .banner__photo::after {
    content: "";
    position: absolute;
    top: 0; right: 0; bottom: 0;
    width: 420px;
    background: linear-gradient(180deg,
      #1f3a30 0%, var(--band-olive) 35%, #b7a86a 65%, var(--band-cream) 100%);
  }
  .discount-badge {
    position: absolute;
    left: 490px;
    top: 6px;
    width: 320px;
    height: 320px;
  }
  .cta-button {
    position: absolute;
    right: 12px;
    bottom: 0;
    width: 270px;
    height: 70px;
    box-sizing: border-box;
    padding: 0 26px;
    display: flex;
    align-items: center;
    justify-content: space-between;
    background: var(--accent);
    color: var(--white);
    border-radius: 10px 10px 0 0;
    font-size: 26px;
    font-weight: 700;
    text-decoration: none;
  }
  .cta-button svg { width: 22px; height: 30px; }
</style>
</head>
<body>
  <div class="banner">
    <div class="banner__photo" role="img" aria-label="Gestapelte Rollen farbiger Gurtbänder in Türkis, Grau, Navy, Braun, Rot, Oliv und gestreift"></div>

    <svg class="discount-badge" viewBox="0 0 320 320" aria-label="Prozent">
      <polygon fill="var(--white)" points="160,0 178,46 212,8 218,58 262,30 252,80 302,68 276,112 320,118 284,152 320,176 280,196 308,236 258,238 276,286 228,272 224,320 186,290 160,318 134,290 96,320 92,272 44,286 62,238 12,236 40,196 0,176 36,152 0,118 44,112 18,68 68,80 58,30 102,58 108,8 142,46"/>
      <polygon fill="var(--accent)" points="160,16 176,58 206,24 210,70 250,46 242,90 288,80 264,118 302,124 270,154 302,176 266,194 292,228 248,230 262,272 220,260 216,302 184,276 160,302 136,276 104,302 100,260 58,272 72,230 28,228 54,194 18,176 50,154 18,124 56,118 32,80 78,90 70,46 110,70 114,24 144,58"/>
      <text x="160" y="212" text-anchor="middle" fill="var(--white)" font-family="Open Sans, Arial, sans-serif" font-weight="600" font-size="160">%</text>
    </svg>

    <a class="cta-button" href="#">
      <span>Restposten</span>
      <svg viewBox="0 0 22 30" aria-hidden="true"><polyline points="5,4 16,15 5,26" fill="none" stroke="var(--white)" stroke-width="4"/></svg>
    </a>
  </div>
</body>
</html>
```